I would like to modify/update my 2 step login screen

I want a more modern looking login page for our document imaging application. I need to keep all of the same elements and buttons that currently exist. The first 2 screens are the login. The 3rd is a screenshot of the actual application home page.

```html
<!DOCTYPE html>
<html lang="en">
<head>
<meta charset="utf-8">
<title>MSDS Login and Home</title>
<link href="https://fonts.googleapis.com/css2?family=Roboto:wght@300;400;500;700&family=Lato:wght@300;400;700&family=Montserrat:wght@600;700&display=swap" rel="stylesheet">
<style>
:root{
  --stage:#000;
  --paper:#fff;
  --navy:#0c4a82;
  --navy-deep:#0a3f70;
  --card:#eef4fb;
  --card-line:#9fb0c4;
  --green:#5cb85c;
  --maroon:#6b0f1a;
  --ink:#333;
  --muted:#666;
  --link:#1a8fd6;
  --sky:#1a9ee0;
  --appbar:#3a3a3a;
  --beta:#f07c1c;
  --brand-red:#8a1c22;
  --nav-red:#c0272d;
  --panel:#f5f5f5;
  --line:#ddd;
  --teal:#2b8fa8;
  --gold:#e6b520;
  --rose:#b83a3a;
}
*{box-sizing:border-box;margin:0;padding:0}
html,body{width:682px;height:1200px;overflow:hidden;background:var(--stage)}
body{position:relative;font-family:"Roboto",Arial,sans-serif;color:var(--ink)}
.screen{position:absolute;left:57px;width:572px;height:344px;background:var(--paper);overflow:hidden}
.screen--sso{top:46px}
.screen--classic{top:419px}
.screen--home{top:792px;background:var(--panel)}
.site-footer{position:absolute;left:0;right:0;bottom:0;height:27px;background:var(--navy);color:#fff;text-align:center}
.site-footer .links{font-size:6px;padding-top:5px}
.site-footer .links span{opacity:.6;margin:0 2px}
.site-footer .copy{font-size:3.6px;margin-top:2px}

.login-card{position:absolute;top:23px;width:164px;height:278px;background:var(--card);border:1px solid var(--card-line);border-radius:4px;overflow:hidden}
.screen--sso .login-card{left:202px}
.screen--classic .login-card{left:204px}
.login-card__head{height:76px;background:var(--navy);display:flex;align-items:center;justify-content:center;gap:4px}
.brand-mark{width:9px;height:9px;background:#fff}
.brand-name{color:#fff;font-size:8px;font-weight:700;letter-spacing:.2px;line-height:1}
.login-title{position:absolute;top:86px;width:100%;text-align:center;font-size:11px;color:#444}
.field{position:absolute;left:18px;width:131px;background:#fff;border:1px solid #9aa;border-radius:3px;font-size:5.6px;color:#666;display:flex;align-items:center}
.field--center{justify-content:center}
.field--left{padding-left:4px}
.btn{position:absolute;left:18px;width:131px;border-radius:9px;font-size:5.6px;display:flex;align-items:center;justify-content:center;gap:4px}
.btn--green{background:var(--green);color:#fff;font-weight:700}
.btn--maroon{background:var(--maroon);color:#fff;font-weight:700}
.btn--outline{background:#fff;border:1px solid #999;color:#555}
.btn-icon{width:8px;height:8px;display:inline-block}
.sq{background:#333}
.ci{border:1.4px solid #333;border-radius:50%}
.or{position:absolute;width:100%;text-align:center;font-size:5.4px;color:#555}
.notice{position:absolute;top:219px;width:100%;text-align:center;font-size:4.6px;font-weight:700;color:#555;line-height:7px}
.forgot{position:absolute;left:18px;top:191px;font-size:5.8px;font-weight:700;color:var(--link)}
.lang{position:absolute;width:100%;text-align:center;font-size:5px;color:#777;display:flex;justify-content:center;align-items:center;gap:3px}
.lang b{color:#444}
.flag{width:7px;height:5px;background:#1f3f8a;border:1px solid #c22}
.lang i{color:#bbb;font-style:normal}

.topstrip{position:absolute;top:0;left:0;right:0;height:20px;background:var(--navy);font-family:"Montserrat",sans-serif;color:#fff}
.topstrip .phone{position:absolute;left:356px;top:6px;font-size:6px;font-weight:600;display:flex;gap:4px;align-items:center}
.pill{position:absolute;top:4px;height:12px;border-radius:6px;font-size:5.3px;font-weight:700;display:flex;align-items:center;justify-content:center;letter-spacing:.3px}
.pill--quote{left:421px;width:53px;background:#fff;color:var(--navy)}
.pill--explore{left:480px;width:69px;background:var(--sky);color:#fff}
.sitenav{position:absolute;top:20px;left:0;right:0;height:38px;background:#eaf2fb}
.sitenav .brand{position:absolute;left:23px;top:14px;display:flex;gap:4px;align-items:center;font-family:"Roboto",sans-serif;font-size:10px;font-weight:700;color:var(--brand-red)}
.sitenav .brand .brand-mark{background:var(--brand-red);width:10px;height:10px}
.sitenav ul{list-style:none;position:absolute;top:17px;left:239px;display:flex;gap:0;font-family:"Montserrat",sans-serif;font-size:7.2px;font-weight:700;color:#555}
.sitenav li{margin-right:21px}
.sitenav li.on{color:var(--nav-red)}
.appbar{position:absolute;top:58px;left:0;right:0;height:13px;background:var(--appbar);color:#fff;font-family:"Lato",sans-serif;font-size:5.2px;display:flex;align-items:center}
.appbar span{margin-left:7px}
.appbar .beta{position:absolute;left:309px;width:107px;height:13px;background:var(--beta);display:flex;align-items:center;justify-content:center;margin:0}
.appbar .right{position:absolute;right:4px;display:flex;gap:9px;align-items:center}
.appbar .smile{width:7px;height:7px;border:1px solid #fff;border-radius:50%}

.app{font-family:"Lato",sans-serif}
.profile{position:absolute;left:7px;top:74px;width:104px;height:45px;background:#6db34a;color:#fff;padding:8px 0 0 8px;font-size:7px;line-height:9.6px}
.tile{position:absolute;width:51px;height:51px;color:#fff;font-size:5px;display:flex;flex-direction:column;align-items:center;justify-content:flex-end;padding-bottom:6px;gap:6px}
.tile svg{width:22px;height:22px}
.toolbar{position:absolute;left:277px;top:79px;display:flex;gap:5px}
.toolbar i{width:10px;height:11px;border:1px solid #c8c8c8;border-radius:2px;display:block}
.widget{position:absolute;background:#fff;border:1px solid #e6e6e6}
.widget h3{font-weight:400;font-size:6.8px;color:#555;padding:6px 5px 4px;border-bottom:2px solid var(--accent);position:relative}
.widget h3::after{content:"⌃ ⊗";position:absolute;right:5px;top:6px;font-size:5px;color:#aaa}
.search{margin:4px 5px;width:90px;height:8px;border:1px solid #ddd;font-size:4.4px;color:#aaa;padding-left:8px;line-height:7px}
table{border-collapse:collapse;margin:0 5px;width:calc(100% - 10px);font-size:5px;color:#555;table-layout:fixed}
th{font-weight:400;text-align:left;border:1px solid #e3e3e3;padding:1px 2px;color:#333;height:9px}
td{border-bottom:1px solid #eee;padding:1px 2px;height:9.5px;white-space:nowrap;overflow:hidden}
.mini{display:inline-block;background:var(--green);color:#fff;font-size:5px;padding:2px 4px;margin:4px 0 0 5px}
.hscroll{margin:2px 5px 0;height:5px;background:#f0f0f0;border:1px solid #ddd;position:relative}
.hscroll::after{content:"";position:absolute;left:6px;top:1px;width:60%;height:2px;background:#bbb}
.cal-bar{display:flex;justify-content:space-between;margin:5px 5px 0}
.cal-range{background:var(--green);color:#fff;font-size:5px;width:86px;height:9px;display:flex;align-items:center;justify-content:space-between;padding:0 4px}
.cal-views{display:flex;gap:1px;font-size:5px}
.cal-views span{background:var(--green);color:#fff;padding:2px 3px}
.cal-days{display:flex;margin:4px 5px 0 42px;font-size:4.4px;color:#555}
.cal-days span{flex:1;text-align:center}
.cal-days .today{color:var(--gold);border-bottom:1px solid var(--gold)}
.cal-side{font-size:4.2px;color:#555;margin:5px 0 0 17px;line-height:6px}
.chat{position:absolute;left:554px;top:290px;width:22px;height:22px;border-radius:50%;background:var(--link);display:flex;align-items:center;justify-content:center}
.chat::after{content:"";width:8px;height:6px;background:#fff;border-radius:2px}
.vscroll{position:absolute;left:566px;top:73px;width:5px;height:244px;background:#eee}
.vscroll::after{content:"";position:absolute;top:8px;left:1px;width:3px;height:86px;background:#bbb}
</style>
</head>
<body>

<section class="screen screen--sso">
  <div class="login-card">
    <div class="login-card__head"><span class="brand-mark"></span><span class="brand-name">MERIDIAN SYSTEMS</span></div>
    <h1 class="login-title">MSDS Login</h1>
    <div class="field field--center" style="top:102px;height:17px">Enter Database</div>
    <div class="btn btn--green" style="top:122px;height:16px">
      <svg class="btn-icon" viewBox="0 0 10 10"><circle cx="4" cy="4" r="3" fill="none" stroke="#fff" stroke-width="1.3"/><line x1="6.2" y1="6.2" x2="9" y2="9" stroke="#fff" stroke-width="1.3"/></svg>
      Log in with my MSView</div>
    <div class="or" style="top:143px">or</div>
    <div class="btn btn--outline" style="top:153px;height:17px"><span class="btn-icon ci"></span>Log in with Lumen ID</div>
    <div class="btn btn--outline" style="top:175px;height:17px"><span class="btn-icon sq"></span>Log in with Vantage</div>
    <div class="btn btn--outline" style="top:196px;height:17px">
      <svg class="btn-icon" viewBox="0 0 8 10"><rect x="1" y="0.5" width="6" height="9" rx="1" fill="none" stroke="#333"/><line x1="3" y1="8" x2="5" y2="8" stroke="#333"/></svg>
      Log in with a one-time code</div>
    <p class="notice">All activity on this site is being recorded.<br>Your IP address is being saved as ‘192.168.168.134’.</p>
    <div class="lang" style="top:260px"><span class="flag"></span>⌵ <b>English</b><i>|</i>Français<i>|</i>Español<i>|</i>中文</div>
  </div>
  <footer class="site-footer"><div class="links">Privacy<span>|</span>Remote Support<span>|</span>Contact Us</div><div class="copy">Copyright &nbsp; 2007-2024. Meridian Systems</div></footer>
</section>

<section class="screen screen--classic">
  <div class="login-card">
    <div class="login-card__head"><span class="brand-mark"></span><span class="brand-name">MERIDIAN SYSTEMS</span></div>
    <h1 class="login-title">Classic Login</h1>
    <div class="field field--left" style="top:104px;height:24px">Enter Username</div>
    <div class="field field--left" style="top:133px;height:24px">Enter your password</div>
    <div class="btn btn--green" style="top:168px;height:17px">Log In</div>
    <a class="forgot">Forgot password?</a>
    <div class="or" style="top:201px">or</div>
    <div class="btn btn--maroon" style="top:217px;height:17px">Log In with MSDSDEMO23</div>
    <div class="lang" style="top:259px"><span class="flag"></span>⌵ <b>English</b><i>|</i>Français<i>|</i>Español<i>|</i>中文</div>
  </div>
  <footer class="site-footer"><div class="links">Privacy<span>|</span>Remote Support<span>|</span>Contact Us</div><div class="copy">Copyright &nbsp; 2007-2024. Meridian Systems</div></footer>
</section>

<section class="screen screen--home app">
  <div class="topstrip">
    <div class="phone">
      <svg width="7" height="7" viewBox="0 0 10 10"><path d="M2 1l2 2-1 1.5c.8 1.5 1.8 2.5 3 3L7.5 6l2 2-1.5 1.5C4.5 9 1 5.5.5 2.5z" fill="none" stroke="#fff" stroke-width=".8"/></svg>
      (555) 010-2747 →</div>
    <div class="pill pill--quote">GET A QUOTE</div>
    <div class="pill pill--explore">EXPLORE SERVICES</div>
  </div>
  <nav class="sitenav">
    <div class="brand"><span class="brand-mark"></span>MERIDIAN SYSTEMS</div>
    <ul><li>HOME</li><li>ABOUT</li><li class="on">SERVICES</li><li>SUPPORT</li><li>SCHOOLS</li><li>MUNICIPALITIES</li></ul>
  </nav>
  <div class="appbar">
    <span style="margin-left:4px">Home</span><span>Search</span><span>Notifications</span><span>Workflow</span><span>Tools ▾</span><span>Admin ▾</span><span>Log Out</span><span>MSDSDEMO23</span>
    <span class="beta">This is a beta version of MSView (WEB203)</span>
    <div class="right"><i class="smile"></i><span style="margin:0">Help ▾</span><span style="margin:0">MSADMIN ▾</span></div>
  </div>

  <div class="profile">MSDSDEMO23<br>msAdmin MSDS<br>staff@msview.com</div>
  <div class="tile" style="left:7px;top:121px;background:#f08a24"><svg viewBox="0 0 24 24" fill="none" stroke="#fff" stroke-width="1.4"><circle cx="12" cy="13" r="8"/><path d="M12 13l-3-4M10 3h4"/></svg>Timesheets</div>
  <div class="tile" style="left:60px;top:121px;background:#e05c5c"><svg viewBox="0 0 24 24" fill="none" stroke="#fff" stroke-width="1.4"><path d="M4 14v-3a8 8 0 0116 0v3"/><rect x="3" y="13" width="4" height="6" rx="1"/><rect x="17" y="13" width="4" height="6" rx="1"/></svg>MSSupport</div>
  <div class="tile" style="left:7px;top:173px;background:#3aa0b8"><svg viewBox="0 0 24 24" fill="none" stroke="#fff" stroke-width="1.4"><circle cx="12" cy="12" r="9"/><circle cx="12" cy="10" r="3"/></svg>Requisitions</div>
  <div class="tile" style="left:60px;top:173px;background:#f2b521"><svg viewBox="0 0 24 24" fill="none" stroke="#fff" stroke-width="1.4"><path d="M6 3h9l4 4v14H6z"/><circle cx="13" cy="14" r="3"/><path d="M15 16l3 3"/></svg>Record Search</div>
  <div class="tile" style="left:7px;top:226px;background:#c9383a"><svg viewBox="0 0 24 24" fill="none" stroke="#fff" stroke-width="1.4"><rect x="6" y="2" width="12" height="8"/><path d="M12 10v4M5 14h14M5 14v3M12 14v3M19 14v3"/><rect x="3" y="17" width="4" height="4"/><rect x="10" y="17" width="4" height="4"/><rect x="17" y="17" width="4" height="4"/></svg>Workflow</div>
  <div class="tile" style="left:60px;top:226px;background:#7ab648"><svg viewBox="0 0 24 24" fill="none" stroke="#fff" stroke-width="1.4"><path d="M5 3h10l4 4v14H5zM8 10h8M8 13h8M8 16h5"/></svg>Expenses/Mileage</div>
  <div class="tile" style="left:7px;top:278px;background:#4a78c0;justify-content:flex-start;padding-top:8px"><svg viewBox="0 0 24 24" fill="none" stroke="#fff" stroke-width="1.4"><rect x="5" y="4" width="14" height="17"/><path d="M9 3h6v3H9zM8 10h8M8 13h8M8 16h8"/></svg>Checklists</div>
  <div class="tile" style="left:60px;top:278px;background:#2fbfb0;justify-content:flex-start;padding-top:8px"><svg viewBox="0 0 24 24" fill="none" stroke="#fff" stroke-width="1.4"><circle cx="7" cy="8" r="2.5"/><circle cx="12" cy="7" r="2.5"/><circle cx="17" cy="8" r="2.5"/><path d="M3 18v-4h8v4M9 17v-4h6v4M13 18v-4h8v4"/></svg>Employee Hub</div>

  <div class="toolbar"><i></i><i></i><i></i><i></i><i></i><i></i><i></i><i></i><i></i><i></i><i></i></div>

  <div class="widget" style="left:127px;top:96px;width:208px;height:134px;--accent:var(--teal)">
    <h3>MY FORMS</h3>
    <div class="search">Enter text to search...</div>
    <table>
      <colgroup><col style="width:27%"><col style="width:47%"><col></colgroup>
      <tr><th>Type</th><th>Description</th><th>Created Date</th></tr>
      <tr><td>Driver's License (or S...</td><td>Mark, Dorsey, 9/4/2000</td><td>10/11/2024, 9:31 AM</td></tr>
      <tr><td>Maintenance Work ...</td><td>Mark, Dorsey, mdorsey@msview.com</td><td>9/17/2024, 2:11 PM</td></tr>
      <tr><td>Budget and Purpose ...</td><td>Hollander, Troy, thol@msview.com</td><td>9/10/2024, 3:44 PM</td></tr>
      <tr><td>Budget and Purpose ...</td><td>Holland, Troy, thol@msview.com</td><td>9/10/2024, 3:42 PM</td></tr>
      <tr><td>Budget and Purpose ...</td><td>Holm, Troy, thol@msview.com</td><td>9/10/2024, 3:40 PM</td></tr>
      <tr><td>Public Records Requ...</td><td>Eric, Laval, 08/28/2024</td><td>8/28/2024, 7:42 AM</td></tr>
      <tr><td>Public Records Requ...</td><td></td><td>8/23/2024, 8:40 AM</td></tr>
    </table>
    <div class="hscroll"></div>
    <span class="mini">New Form ▾</span> <span class="mini" style="margin-left:1px">Edit Form</span>
  </div>

  <div class="widget" style="left:340px;top:96px;width:208px;height:134px;--accent:var(--gold)">
    <h3>CREATE FORMS</h3>
    <table style="margin-top:3px">
      <tr><th>Document Type</th><th>Description</th></tr>
      <tr><td>Administrative Leadership Salary Notice</td><td>Administrative Leadership Salary Notice</td></tr>
      <tr><td>Administrator Contract</td><td>Administrator Contract</td></tr>
      <tr><td>Application</td><td>Application</td></tr>
      <tr><td>Athletics Contract Certified</td><td>Athletics Contract Certified</td></tr>
      <tr><td>Athletics Contract Non-Teaching</td><td>Athletics Contract Non-Teaching</td></tr>
      <tr><td>AUP Staff Network Acceptable Use Agreement</td><td>AUP Staff Network Acceptable Use Agreement</td></tr>
      <tr><td>Budget and Purpose Statement</td><td>Budget and Purpose Statement</td></tr>
      <tr><td>Certificated Substitute</td><td>Certificated Substitute</td></tr>
    </table>
    <div class="hscroll"></div>
    <span class="mini">New Form</span>
  </div>

  <div class="widget" style="left:127px;top:236px;width:208px;height:90px;--accent:var(--green)">
    <h3>CALENDAR</h3>
    <div class="cal-bar">
      <div class="cal-range"><span>‹</span>14-18 October 2024<span>›</span></div>
      <div class="cal-views"><span>Day</span><span>Work Week</span><span>Month</span></div>
    </div>
    <div class="cal-days"><span>Mon 14</span><span>Tue 15</span><span>Wed 16</span><span class="today">Thu 17</span><span>Fri 18</span></div>
    <div class="cal-side"><b>All day</b><br>12:00 AM</div>
  </div>

  <div class="widget" style="left:340px;top:236px;width:208px;height:90px;--accent:var(--rose)">
    <h3>WORKFLOW SUMMARY</h3>
    <table style="margin-top:3px">
      <colgroup><col style="width:80%"><col></colgroup>
      <tr><th>Queue</th><th>Items</th></tr>
      <tr><td>AP Workflow: Invoice Added</td><td>2</td></tr>
      <tr><td>AP Workflow: Invoice Approved</td><td>3</td></tr>
      <tr><td>AP Workflow: Ready to Pay/Print</td><td>4</td></tr>
      <tr><td>AP Workflow: Then &amp; Now</td><td>2</td></tr>
      <tr><td>AP Workflow: Invoices - Explain Then &amp; Now</td><td>1</td></tr>
    </table>
  </div>

  <div class="vscroll"></div>
  <div class="chat"></div>
  <footer class="site-footer" style="font-family:Roboto,sans-serif"><div class="links">Privacy<span>|</span>Remote Support<span>|</span>Contact Us</div><div class="copy">Copyright &nbsp; 2007-2024. Meridian Systems</div></footer>
</section>

</body>
</html>
```